All-natural soap packaging design for new company

The box type has been selected, we just need artwork for each of our 10 products. I'd like the same look to each, the idea is just to switch out the name and ingredient label on each. The dimensions are 3.5"x3.75"x1.25". The colors in the uploaded pictures with product titles are not mandatory. I'd like to keep the font on the packaging (Rubik) as it is the same as the website.

Target Market(s)

Health & Beauty, people looking for natural or organic products

Industry/Entity Type

It Company

Colors

Designer to choose colors to be used in the design.

Requirements
Must have
• Design must be clean and relatively simple. Slightly different look for each of the 10 products. Audience is people looking for all-natural products.

```html
<!DOCTYPE html>
<html lang="en">
<head>
<meta charset="utf-8">
<title>Handmade Soap – Lavender Witch Hazel</title>
<link href="https://fonts.googleapis.com/css2?family=Rubik:wght@400;500&display=swap" rel="stylesheet">
<style>
  :root {
    --backdrop: #efeff0;
    --kraft: #dcb77c;
    --kraft-dark: #d2ab6e;
    --band: #ffffff;
    --ink: #1c1c1c;
    --brand-blue: #2f7fd1;
    --lavender-deep: #6a4f9c;
    --lavender-light: #a88fd0;
    --stem: #7d9a55;
  }
  * { margin: 0; padding: 0; box-sizing: border-box; }
  html, body {
    width: 1200px; height: 880px; overflow: hidden;
    background: var(--backdrop);
    font-family: "Rubik", sans-serif;
  }
  .box-front {
    position: absolute; left: 190px; top: 130px;
    width: 820px; height: 620px;
    background: linear-gradient(180deg, var(--kraft) 0%, var(--kraft-dark) 100%);
    overflow: hidden;
  }
  .white-band {
    position: absolute; left: 0; right: 0; top: 170px; height: 290px;
    background: var(--band);
    border-top: 2px solid var(--ink);
    border-bottom: 2px solid var(--ink);
  }
  .label-frame {
    position: absolute; left: 80px; top: 20px; width: 660px; height: 580px;
  }
  .label-content {
    position: absolute; left: 80px; top: 20px; width: 660px; height: 580px;
    display: flex; flex-direction: column; align-items: center;
    color: var(--ink); text-align: center;
  }
  .brand {
    margin-top: 72px;
    display: flex; align-items: center; gap: 8px;
    font-size: 15px; font-weight: 500; letter-spacing: 1px;
    color: var(--ink);
  }
  .brand-square {
    width: 14px; height: 14px; background: var(--brand-blue);
  }
  .claim {
    margin-top: 78px;
    font-size: 26px; font-weight: 400; letter-spacing: 1px;
  }
  .product-title {
    margin-top: 4px;
    font-size: 56px; font-weight: 400; letter-spacing: 1.5px; line-height: 1.1;
  }
  .ingredients {
    margin-top: 18px;
    font-size: 18px; letter-spacing: 1.5px; word-spacing: 10px;
  }
  .herb-photo {
    margin-top: 22px; width: 180px; height: 76px; border-radius: 38px 10px 10px 38px;
    background: linear-gradient(90deg, var(--lavender-deep) 0%, var(--lavender-light) 55%, var(--stem) 100%);
  }
</style>
</head>
<body>
  <div class="box-front">
    <div class="white-band"></div>
    <svg class="label-frame" viewBox="0 0 660 580" aria-hidden="true">
      <defs>
        <path id="label-shape" d="M130 10 H530 V50 H580 V150 Q650 290 580 430 V530 H530 V570 H130 V530 H80 V430 Q10 290 80 150 V50 H130 Z"/>
      </defs>
      <use href="#label-shape" fill="#fff" stroke="#1c1c1c" stroke-width="2"/>
      <use href="#label-shape" fill="#fff" stroke="#1c1c1c" stroke-width="12" transform="translate(330 290) scale(0.93) translate(-330 -290)"/>
    </svg>
    <div class="label-content">
      <div class="brand"><span class="brand-square"></span>ASHFORD SOAP CO.</div>
      <p class="claim">100% NATURAL</p>
      <h1 class="product-title">HANDMADE SOAP</h1>
      <p class="ingredients">LAVENDER WITCH&nbsp;HAZEL</p>
      <div class="herb-photo" role="img" aria-label="Photo of a tied bunch of lavender sprigs"></div>
    </div>
  </div>
</body>
</html>
```